Business Card Design Project 4 Construction Business

I am after a creative, but sleek and simple/ clean business card design. This design will form the basis of future items and might include a logo or simply a creative way to lay out the text of my company name 'kestrel ventures'
I like the simplicity of black and white however I would also be happy to see a splash of colour introduced somehow to give the text some interest and make it stand out.
I would like a double sided card.
I am young (ish!) and professional, offering construction and project management services, what I don't want is the traditional builders type card featuring a cheesy hammer/ saw image etc.
As the company name, kestrel ventures, suggests, we focus on working closely and collaboratively together, in synergy with all stakeholders involved in the projects that we undertake
Construction

```html
<!DOCTYPE html>
<html lang="en">
<head>
<meta charset="utf-8">
<title>Kestrel Ventures – Business Card</title>
<link rel="stylesheet" href="https://fonts.googleapis.com/css2?family=Michroma&family=Questrial&display=swap">
<style>
  :root {
    --page-bg: #141414;
    --card-black: #0f0f0f;
    --silver-light: #d9dadb;
    --silver-mid: #9a9b9d;
    --silver-dark: #6a6b6d;
    --brand-orange: #f08222;
    --brand-orange-deep: #d86f18;
    --brand-bronze: #b06a2a;
    --ink-white: #fff7ee;
    --shadow: rgba(0, 0, 0, 0.6);
  }
  * { box-sizing: border-box; margin: 0; padding: 0; }
  html, body {
    width: 1200px;
    height: 900px;
    overflow: hidden;
    background: radial-gradient(ellipse at 50% 40%, #222 0%, var(--page-bg) 70%);
  }
  .canvas {
    position: relative;
    width: 1200px;
    height: 900px;
  }
  .card {
    position: absolute;
    left: 250px;
    width: 700px;
    height: 400px;
    overflow: hidden;
    box-shadow: 0 18px 40px var(--shadow);
  }

  /* Front side */
  .card--front {
    top: 40px;
    background: var(--card-black);
  }
  .front__silver {
    position: absolute;
    left: 0; top: 0;
    width: 300px; height: 100%;
    background: radial-gradient(circle at 30% 20%, var(--silver-light) 0%, var(--silver-mid) 45%, var(--silver-dark) 100%);
  }
  .front__mark {
    position: absolute;
    left: 205px; top: 250px;
    width: 70px; height: 70px;
    border-radius: 12px;
    background: var(--brand-orange);
  }
  .front__name {
    position: absolute;
    left: 340px; top: 182px;
    font-family: "Michroma", sans-serif;
    font-size: 27px;
    letter-spacing: 1px;
    color: var(--brand-bronze);
    white-space: nowrap;
  }

  /* Back side */
  .card--back {
    top: 460px;
    background: linear-gradient(100deg, var(--brand-orange) 0%, var(--brand-orange) 60%, var(--brand-orange-deep) 100%);
    font-family: "Questrial", sans-serif;
    color: var(--ink-white);
  }
  .back__faint-square {
    position: absolute;
    left: 90px; top: 80px;
    width: 170px; height: 150px;
    border-radius: 22px;
    background: rgba(120, 60, 10, 0.22);
  }
  .back__person {
    position: absolute;
    left: 330px; top: 58px;
    font-size: 22px;
    letter-spacing: 1px;
  }
  .back__role {
    font-size: 11px;
    margin-left: 28px;
    vertical-align: middle;
    opacity: 0.9;
  }
  .back__details {
    position: absolute;
    left: 200px; top: 118px;
    display: grid;
    grid-template-columns: 110px auto;
    row-gap: 6px;
    font-size: 18px;
    letter-spacing: 0.5px;
  }
  .back__label { text-align: right; padding-right: 18px; }
  .back__gap { height: 18px; }
</style>
</head>
<body>
<main class="canvas">
  <section class="card card--front" aria-label="Card front">
    <div class="front__silver"></div>
    <div class="front__mark"></div>
    <h1 class="front__name">Kestrel Ventures</h1>
  </section>

  <section class="card card--back" aria-label="Card back">
    <div class="back__faint-square"></div>
    <p class="back__person">Aaron Whitfield <span class="back__role">[ director ]</span></p>
    <div class="back__details">
      <span class="back__label">address.</span>
      <span>5678 Larkspur Avenue, Suite B<br>Oakland, CA 5678</span>
      <span class="back__gap"></span><span class="back__gap"></span>
      <span class="back__label">ph.number.</span>
      <span>098.765.4321</span>
      <span class="back__gap"></span><span class="back__gap"></span>
      <span class="back__label">e-mail.</span>
      <span>mymail@kestrelventures.com</span>
      <span class="back__label">website.</span>
      <span>www.kestrelventures.com</span>
    </div>
  </section>
</main>
</body>
</html>
```